Company Stationary

I'd like a template to use for company stationery. We frequently write short 1 - 2 page Word documents (which we save as PDF) to clients and prospects and the presentation is boring and doesn't look professional. I am looking for a Word template that will convey a better sense of professionalism. The design should include our logo (attached) but be simple and elegant. It should save nicely as a PDF, since that is how we will send the files via email.

Target Market(s)

Financial Institutions

Industry/Entity Type

Financial Service

Font styles to use
Serif

Colors

Designer to choose colors to be used in the design.

Requirements
Must have
• Simple design. Needs to be subtle. I don't want the design to be more interesting than the message we are writing.
Nice to have
• When the reader sees it, I want them to feel they are reading something published by a large, very successful company.
Should not have
• Not overpowering design and colors.

```html
<!DOCTYPE html>
<html lang="en">
<head>
<meta charset="utf-8">
<title>Clearwell Letterhead</title>
<link href="https://fonts.googleapis.com/css2?family=Lato:wght@400;700;900&family=Open+Sans:wght@400&display=swap" rel="stylesheet">
<style>
  :root {
    --backdrop: #e9e9e9;
    --paper: #ffffff;
    --ink: #111111;
    --rule: #6d6d6d;
    --accent: #ee1c0e;
    --band-dark: #0c0c0c;
    --signature-tone: #e4e4e4;
  }
  * { margin: 0; padding: 0; box-sizing: border-box; }
  html, body {
    width: 1200px; height: 815px; overflow: hidden;
    background: var(--backdrop);
  }
  .canvas { position: relative; width: 1200px; height: 815px; }

  .sheet {
    position: absolute; width: 490px; height: 690px;
    background: var(--paper);
  }
  .sheet--letter { left: 80px; top: 64px; }
  .sheet--blank  { left: 636px; top: 69px; }

  .brand {
    position: absolute; top: 26px; left: 0; width: 100%;
    display: flex; justify-content: center; align-items: center; gap: 8px;
    font-family: "Lato", sans-serif; font-weight: 900;
    font-size: 32px; letter-spacing: 0.5px; color: var(--ink);
  }
  .brand__mark { width: 12px; height: 12px; background: var(--accent); }

  .rule {
    position: absolute; left: 32px; width: 425px; height: 1px;
    background: var(--rule);
  }
  .rule--header { top: 78px; }
  .rule--footer { top: 639px; }

  .letter-body {
    position: absolute; top: 169px; left: 32px; width: 362px;
    font-family: "Open Sans", sans-serif; font-size: 7.4px; line-height: 11.6px;
    color: var(--ink);
  }
  .letter-body p + p { margin-top: 11.6px; }

  .signature {
    position: absolute; top: 448px; left: 36px; width: 140px; height: 26px;
    background: var(--signature-tone); border-radius: 3px;
  }

  .contact {
    position: absolute; left: 0; width: 100%; text-align: center;
    font-family: "Lato", sans-serif; font-size: 9px; color: var(--ink);
  }
  .contact--address { top: 647px; }
  .contact--lines {
    top: 663px; display: flex; justify-content: center; align-items: center; gap: 4px;
  }
  .contact__icon { width: 7px; height: 7px; fill: var(--accent); }
  .contact__item { margin-right: 3px; }

  .band {
    position: absolute; bottom: 0; left: 0; width: 100%; height: 9px;
    display: flex; gap: 3px;
  }
  .band__red { flex: 1; background: var(--accent); }
  .band__dark { flex: 1; background: var(--band-dark); }
</style>
</head>
<body>
<div class="canvas">

  <section class="sheet sheet--letter">
    <div class="brand"><span class="brand__name">Clearwell</span><span class="brand__mark"></span></div>
    <div class="rule rule--header"></div>

    <div class="letter-body">
      <p>Lorem ipsum dolor sit amet, consectetur adipiscing elit. Praesent non est diam. Vivamus risus sem, gravida sit amet nibh ut, ornare lobortis ante. Aliquam sollicitudin, mauris tincidunt semper venenatis, orci est pretium augue, ut vestibulum felis velit bibendum urna. Integer sollicitudin aliquet ligula, non ultricies nisl efficitur nec. Aliquam felis lorem, facilisis ac condimentum quis, consectetur volutpat lacus. Proin fermentum sem quis elit efficitur, eu tempus magna maximus.</p>
      <p>Aenean a mi tortor. Morbi pretium mi sed cursus vehicula. Lorem ipsum dolor sit amet, consectetur adipiscing elit. In finibus eros ac maximus finibus. Nunc pretium pellentesque tellus. Nullam accumsan nisl non diam commodo sagittis. Nunc et ante sit amet urna auctor convallis. Maecenas sed fringilla metus, sit amet vulputate felis. Morbi eget tempor nisi. Aliquam erat volutpat. Aenean laoreet interdum tempus.</p>
      <p>Maecenas dignissim placerat mauris, vitae sollicitudin ex. Integer bibendum maximus mauris, ac tempor urna viverra id. Integer tincidunt lobortis nisl at posuere. Sed faucibus vulputate finibus. Maecenas convallis, sem quis pellentesque cursus, urna quam aliquam augue, quis porttitor eros est nec lectus. Sed mattis at tellus ut blandit. Aenean nunc magna, viverra sed mauris vel, porta finibus lacus. Nullam bibendum turpis rutrum porta placerat</p>
      <p>Aenean a mi tortor. Morbi pretium mi sed cursus vehicula. Lorem ipsum dolor sit amet, consectetur adipiscing elit. In finibus eros ac maximus finibus. Nunc pretium pellentesque tellus. Nullam accumsan nisl non diam commodo sagittis. Nunc et ante sit amet urna auctor convallis. Maecenas sed fringilla metus, sit amet vulputate felis. Morbi eget tempor nisi. Aliquam erat volutpat. Aenean laoreet interdum tempus. .</p>
    </div>

    <div class="signature" role="img" aria-label="Handwritten signature of the sender"></div>

    <div class="rule rule--footer"></div>
    <p class="contact contact--address">Clearwell, LLC, 218 Harbor Lane, Fairview, NJ 07022</p>
    <div class="contact contact--lines">
      <svg class="contact__icon" viewBox="0 0 10 10"><path d="M2 0.5 L3.8 2.6 L2.9 3.8 Q4 6 6.2 7.1 L7.4 6.2 L9.5 8 L8.2 9.5 Q4.5 9.5 1.8 6.5 Q0 4 0.5 1.8 Z"/></svg>
      <span class="contact__item">555 010 4200</span>
      <svg class="contact__icon" viewBox="0 0 10 10"><rect x="2" y="0" width="6" height="3"/><rect x="0" y="3.5" width="10" height="4" rx="1"/><rect x="2" y="8" width="6" height="2"/></svg>
      <span class="contact__item">555 010 4201</span>
      <svg class="contact__icon" viewBox="0 0 10 10"><rect x="0" y="2" width="10" height="6.5"/><path d="M0 2 L5 6 L10 2" fill="none" stroke="#fff" stroke-width="1"/></svg>
      <span class="contact__item">info@clearwellgroup.com</span>
      <svg class="contact__icon" viewBox="0 0 10 10"><circle cx="5" cy="5" r="4.6"/><path d="M0.5 5 H9.5 M5 0.5 V9.5 M5 0.5 Q2 5 5 9.5 M5 0.5 Q8 5 5 9.5" fill="none" stroke="#fff" stroke-width="0.6"/></svg>
      <span class="contact__item">www.clearwellgroup.com</span>
    </div>
    <div class="band"><span class="band__red"></span><span class="band__dark"></span></div>
  </section>

  <section class="sheet sheet--blank">
    <div class="brand"><span class="brand__name">Clearwell</span><span class="brand__mark"></span></div>
    <div class="rule rule--header"></div>

    <div class="rule rule--footer"></div>
    <p class="contact contact--address">Clearwell, LLC, 218 Harbor Lane, Fairview, NJ 07022</p>
    <div class="contact contact--lines">
      <svg class="contact__icon" viewBox="0 0 10 10"><path d="M2 0.5 L3.8 2.6 L2.9 3.8 Q4 6 6.2 7.1 L7.4 6.2 L9.5 8 L8.2 9.5 Q4.5 9.5 1.8 6.5 Q0 4 0.5 1.8 Z"/></svg>
      <span class="contact__item">555 010 4200</span>
      <svg class="contact__icon" viewBox="0 0 10 10"><rect x="2" y="0" width="6" height="3"/><rect x="0" y="3.5" width="10" height="4" rx="1"/><rect x="2" y="8" width="6" height="2"/></svg>
      <span class="contact__item">555 010 4201</span>
      <svg class="contact__icon" viewBox="0 0 10 10"><rect x="0" y="2" width="10" height="6.5"/><path d="M0 2 L5 6 L10 2" fill="none" stroke="#fff" stroke-width="1"/></svg>
      <span class="contact__item">info@clearwellgroup.com</span>
      <svg class="contact__icon" viewBox="0 0 10 10"><circle cx="5" cy="5" r="4.6"/><path d="M0.5 5 H9.5 M5 0.5 V9.5 M5 0.5 Q2 5 5 9.5 M5 0.5 Q8 5 5 9.5" fill="none" stroke="#fff" stroke-width="0.6"/></svg>
      <span class="contact__item">www.clearwellgroup.com</span>
    </div>
    <div class="band"><span class="band__red"></span><span class="band__dark"></span></div>
  </section>

</div>
</body>
</html>
```